Namibia currently imports 60% of its food. Yield Forward Tarvenia is an initiative which will assist Namibia to become self sustainable in terms of food production. We aim to do this through the development of 3 agricultural production zones which will include farming zones, local farmer assistance, processing and distribution of the final products. Please see our project overview attached.

```html
<!DOCTYPE html>
<html lang="en">
<head>
<meta charset="utf-8">
<title>Yield Forward Tarvenia</title>
<link href="https://fonts.googleapis.com/css2?family=Oswald:wght@600&family=Poppins:wght@400;500;600;700&family=Marcellus&display=swap" rel="stylesheet">
<style>
:root{
  --green:#0b6634;
  --blue:#1f8bc9;
  --tan:#c7a482;
  --ink:#1b1b1b;
  --grey-band:#efefef;
  --mint:#bfe5c0;
  --white:#ffffff;
}
*{margin:0;padding:0;box-sizing:border-box}
html,body{width:1200px;height:4520px;overflow:hidden;background:var(--white)}
body{position:relative;font-family:'Poppins',sans-serif;color:var(--ink)}
.abs{position:absolute}
.brand{font-family:'Marcellus',serif;color:var(--green);line-height:1;white-space:nowrap}
.brand-header{left:74px;top:52px;font-size:21px;letter-spacing:.3px}
.brand-footer{left:74px;top:4258px;font-size:20px;letter-spacing:.3px}
.nav{position:absolute;top:50px;right:72px;display:flex;gap:38px;font-size:15px;color:#333}
.nav a{color:inherit;text-decoration:none}
.nav .active{color:var(--green);font-weight:600;border-bottom:2px solid var(--green);padding-bottom:2px}
.photo{position:absolute}
.hero-photo{left:0;top:113px;width:1200px;height:780px;background:linear-gradient(180deg,#7f93a8 0%,#8e9a6a 40%,#6c6a3e 70%,#4f5a33 100%)}
.hero-title{position:absolute;top:365px;left:0;width:1200px;text-align:center;font-family:'Oswald',sans-serif;font-size:92px;color:#fff;letter-spacing:1px;line-height:1}
.hero-sub{position:absolute;top:470px;left:150px;width:900px;text-align:center;font-weight:700;font-size:28px;line-height:38px;color:#fff}
.btn{position:absolute;width:217px;height:56px;border-radius:28px;background:var(--tan);color:#fff;font-weight:700;font-size:16px;text-align:center;line-height:56px}
.h2{position:absolute;font-weight:700;font-size:36px;line-height:42px;letter-spacing:.3px;text-transform:uppercase;color:var(--ink)}
.h2 .accent{color:var(--green)}
.h3{position:absolute;font-weight:700;font-size:35px;line-height:37px;color:var(--blue)}
.copy{position:absolute;font-size:15px;line-height:29.5px;color:#222}
.grey-band{left:0;top:1470px;width:1200px;height:736px;background:var(--grey-band)}
.zone-card{position:absolute;top:1770px;width:330px;height:358px}
.zone-card .pic{position:absolute;left:0;top:0;width:330px;height:300px}
.zone-card .label{position:absolute;left:25px;top:250px;width:280px;height:108px;background:#fff;text-align:center;padding-top:20px;font-weight:600;font-size:26px;line-height:37px}
.zone-card .label .region{color:var(--blue);display:block}
.zone-card .label .area{color:var(--green);display:block;font-size:24px}
.rounded{border-radius:18px}
.mint-band{left:0;top:3280px;width:1200px;height:860px;background:var(--mint)}
.footer-title{position:absolute;font-weight:700;font-size:22px;color:var(--blue)}
.footer-list{position:absolute;list-style:none;font-size:15px;line-height:33px;color:#222}
.footer-small{position:absolute;font-size:14px;line-height:26px;color:#222}
.contact-row{position:absolute;left:795px;font-size:15px;line-height:30px;color:#222}
.contact-row svg{position:absolute;left:0;top:7px}
.contact-row span{display:block;padding-left:33px}
.social{position:absolute;top:4420px;left:74px;display:flex;gap:18px}
.social span{width:24px;height:24px;border-radius:50%;background:var(--green)}
</style>
</head>
<body>

<header>
  <div class="abs brand brand-header">YIELD FORWARD TARVENIA</div>
  <nav class="nav">
    <a class="active">Home</a><a>About Us</a><a>Solutions</a><a>Production Zones</a><a>Latest News</a><a>Contact Us</a>
  </nav>
</header>

<section>
  <div class="photo hero-photo" role="img" aria-label="Farm workers carrying crates of vegetables across a green field"></div>
  <svg class="abs" style="left:0;top:640px" width="1200" height="260" viewBox="0 0 1200 260">
    <path d="M0 255 L0 230 C160 130 300 110 470 150 C650 195 760 210 900 170 C1010 140 1120 100 1200 60 L1200 260 Z" fill="#fff"/>
    <path d="M0 230 C160 130 300 110 470 150 C650 195 760 210 900 170 C1010 140 1120 100 1200 60" fill="none" stroke="var(--green)" stroke-width="14"/>
  </svg>
  <h1 class="hero-title">YIELD FORWARD TARVENIA</h1>
  <p class="hero-sub">Nemo enim ipsam voluptatem quia voluptas sit aspernatur aut odit aut fugit, sed quia consequuntur magni.</p>
  <div class="btn" style="left:492px;top:570px">Read More</div>
</section>

<section>
  <div class="photo" style="left:0;top:958px;width:586px;height:445px;border-radius:0 230px 230px 0;background:linear-gradient(160deg,#9fb6cf 0%,#b7c1c7 35%,#6f7a4a 60%,#7a4f3a 100%)" role="img" aria-label="Farm workers harvesting sweet potatoes into red crates beside a tractor"></div>
  <h2 class="h2" style="left:615px;top:985px">About Yield<br>Forward Tarvenia</h2>
  <p class="copy" style="left:615px;top:1079px;width:515px">Namibia is a young democracy in Sub-Saharan Africa with a population of approximately 2.5 Million people. The country's agricultural sector has been slow to keep up with the increasing population. As a consequence, approximately 60% of the food required to feed the nation is imported. The elevated cost of these imported foods means a large proportion of the population consume food with low nutritional value.</p>
  <div class="btn" style="left:615px;top:1314px">Read More</div>
</section>

<section>
  <div class="abs grey-band"></div>
  <svg class="abs" style="left:0;top:1440px" width="1200" height="200" viewBox="0 0 1200 200">
    <path d="M0 0 L1200 0 L1200 150 C1120 90 1000 40 860 30 C700 20 560 130 380 145 C230 158 100 110 0 50 Z" fill="#fff"/>
    <path d="M0 50 C100 110 230 158 380 145 C560 130 700 20 860 30 C1000 40 1120 90 1200 150" fill="none" stroke="var(--green)" stroke-width="11"/>
  </svg>
  <h2 class="h2" style="left:0;top:1680px;width:1200px;text-align:center"><span class="accent">3 Agricultural</span> Production Zones</h2>

  <div class="zone-card" style="left:74px">
    <div class="pic" role="img" aria-label="Town in a valley with mountains under a blue sky" style="background:linear-gradient(180deg,#8fb1d2 0%,#c9b79b 45%,#6e7f52 100%)"></div>
    <div class="label"><span class="region">Otavi Region</span><span class="area">Central Namibia</span></div>
  </div>
  <div class="zone-card" style="left:436px">
    <div class="pic" role="img" aria-label="Grassland with trees at dusk" style="background:linear-gradient(180deg,#9fb0c8 0%,#d6b7a8 40%,#4e6b35 100%)"></div>
    <div class="label"><span class="region">Kavango Region</span><span class="area">North Namibia</span></div>
  </div>
  <div class="zone-card" style="left:798px">
    <div class="pic" role="img" aria-label="Concrete dam wall holding a reservoir among rocky hills" style="background:linear-gradient(180deg,#3f6fa8 0%,#8b6a52 45%,#bdb7ad 75%,#7a6a55 100%)"></div>
    <div class="label"><span class="region">Neckartal Dam</span><span class="area">South Namibia</span></div>
  </div>
</section>

<section>
  <h2 class="h2" style="left:0;top:2278px;width:1200px;text-align:center"><span class="accent">“Yield Forward”</span> Sustainability</h2>

  <div class="photo rounded" style="left:74px;top:2380px;width:515px;height:386px;background:linear-gradient(135deg,#8fa35c 0%,#5f7a3a 45%,#6f8274 100%)" role="img" aria-label="Woman in a straw hat inspecting maize plants"></div>
  <h3 class="h3" style="left:615px;top:2440px">Processing Facilities</h3>
  <p class="copy" style="left:615px;top:2496px;width:500px">Each of the allocated production zones will be furnished with handling, processing and milling facilities for all crops produced as part of the program. These will include Potatoes, Maize and Wheat.</p>
  <div class="btn" style="left:615px;top:2640px">Read More</div>

  <h3 class="h3" style="left:74px;top:2875px">Sustainable Solutions</h3>
  <p class="copy" style="left:74px;top:2930px;width:515px">All irrigation, cropping and production facilities will be operated “off grid” using extensive solar and hydroelectric power generation. In addition, cropping at all sites will be operated with the use of drones for spraying and crop analysis resulting in significant fuel savings and the associated carbon output.</p>
  <div class="btn" style="left:74px;top:3110px">Read More</div>
  <div class="photo rounded" style="left:612px;top:2830px;width:515px;height:386px;background:linear-gradient(180deg,#6f9bd1 0%,#c9d9e8 30%,#4f6b3a 45%,#8fae4e 70%,#a6bf5a 100%)" role="img" aria-label="Solar panels beyond a field of green wheat"></div>
</section>

<section>
  <div class="abs mint-band"></div>
  <svg class="abs" style="left:0;top:3260px" width="1200" height="180" viewBox="0 0 1200 180">
    <path d="M0 0 L1200 0 L1200 140 C1120 80 1000 35 860 28 C700 20 560 120 380 135 C230 148 100 100 0 40 Z" fill="#fff"/>
    <path d="M0 40 C100 100 230 148 380 135 C560 120 700 20 860 28 C1000 35 1120 80 1200 140" fill="none" stroke="var(--green)" stroke-width="11"/>
  </svg>
  <h2 class="h2" style="left:0;top:3490px;width:1200px;text-align:center"><span class="accent">“Yield Forward”</span> Education</h2>
  <div class="photo rounded" style="left:74px;top:3580px;width:515px;height:386px;background:linear-gradient(135deg,#6f9a48 0%,#4c7a34 50%,#a8b79a 100%)" role="img" aria-label="Young farmer using a tablet in a maize field"></div>
  <h3 class="h3" style="left:615px;top:3585px;width:500px">Give a man a fish and feed him for a day, teach a man to fish and feed him for a lifetime</h3>
  <p class="copy" style="left:615px;top:3742px;width:515px">Education is key to empowerment and we embrace that concept. As such, we aim to offer a vocational education scheme for the participants in the Yield Forward Tarvenia program. We aim to furnish the participants with the skills to be successful and sustainable farmers in their own rights.</p>
  <div class="btn" style="left:615px;top:3912px">Read More</div>
  <svg class="abs" style="left:0;top:3960px" width="1200" height="190" viewBox="0 0 1200 190">
    <path d="M0 40 C120 110 260 150 420 140 C620 128 760 30 930 45 C1050 56 1140 100 1200 140 L1200 190 L0 190 Z" fill="#fff"/>
    <path d="M0 40 C120 110 260 150 420 140 C620 128 760 30 930 45 C1050 56 1140 100 1200 140" fill="none" stroke="var(--green)" stroke-width="11"/>
  </svg>
</section>

<footer>
  <div class="abs brand brand-footer">YIELD FORWARD TARVENIA</div>
  <p class="footer-small" style="left:74px;top:4336px">Copyright © 2024 Harvestline Trust<br>All Rights Reserved</p>
  <div class="social" aria-label="Social links"><span></span><span></span><span></span><span></span><span></span></div>

  <h4 class="footer-title" style="left:459px;top:4210px">Quick Links</h4>
  <ul class="footer-list" style="left:459px;top:4254px">
    <li>Home</li><li>About Us</li><li>Solutions</li><li>Production Zones</li><li>Latest News</li><li>Contact Us</li>
  </ul>

  <h4 class="footer-title" style="left:795px;top:4204px">Contact Us</h4>
  <div class="contact-row" style="top:4250px">
    <svg width="16" height="14" viewBox="0 0 16 14"><path d="M0 2 L5 0 L11 2 L16 0 L16 12 L11 14 L5 12 L0 14 Z" fill="var(--blue)"/></svg>
    <span>48 Marula Court, Suite 12,<br>Windale 20417, Tarvenia</span>
  </div>
  <div class="contact-row" style="top:4320px">
    <svg width="14" height="14" viewBox="0 0 14 14"><path d="M3 0 L5 4 L3.5 5.5 C4.5 7.5 6.5 9.5 8.5 10.5 L10 9 L14 11 L12.5 14 C6 13.5 0.5 8 0 1.5 Z" fill="var(--blue)"/></svg>
    <span>+264-555-0142</span>
  </div>
  <div class="contact-row" style="top:4360px">
    <svg width="15" height="12" viewBox="0 0 15 12"><rect width="15" height="12" rx="1" fill="var(--blue)"/><path d="M0 1 L7.5 7 L15 1" fill="none" stroke="#fff" stroke-width="1.3"/></svg>
    <span>hello@yieldforward.example</span>
  </div>
</footer>

</body>
</html>
```